Real Estate Sales Window Card

We require a Window card for real estate sales and leasing.
K7 Residences is a wool store conversion located in the trendy, riverside suburb of Teneriffe, Brisbane. The clientele are generally professional couples working inner city jobs.
The card should reflect the style and colouring of the existing themes of the building, in particular the simple structural aspects with primary colours of black, white, grey, mocha and olive green.
For more details on the K7 residences please see http://k7residences-example.com.au/about/gallery/apartment-gallery (please note: disregard the red on the site as it is not part of the buildings tones)
The card should contain the following:
- Header
- Price
- Bed, Bath, Car
- Description
- Photo(s)
- Ad type (i.e. Sale or Lease)
The card will be used in A4 portrait and A3 landscape aspects.
Real Estate

```html
<!DOCTYPE html>
<html lang="en">
<head>
<meta charset="utf-8">
<title>K7 Residences – Window Card</title>
<link rel="stylesheet" href="https://fonts.googleapis.com/css2?family=Arimo:wght@400;700&display=swap">
<style>
  :root {
    --stone: #9caaa6;
    --panel: #0a0a0a;
    --white: #ffffff;
    --olive: #6e8d1f;
    --olive-dark: #4d6514;
    --frame: #dfe5e3;
  }
  * { margin: 0; padding: 0; box-sizing: border-box; }
  html, body { width: 848px; height: 1200px; overflow: hidden; }
  body {
    background: var(--stone);
    font-family: "Arimo", Arial, sans-serif;
    color: var(--white);
  }
  .card { position: relative; width: 848px; height: 1200px; }

  .brand {
    position: absolute; left: 68px; top: 34px; width: 173px; height: 182px;
    border: 1px solid var(--frame);
    display: flex; flex-direction: column; align-items: center; justify-content: center;
    text-align: center; padding: 0 10px;
  }
  .brand-name {
    font-weight: 700; font-size: 21px; line-height: 1.15; text-transform: uppercase;
    color: var(--white); white-space: nowrap;
  }
  .brand-architect {
    position: absolute; left: 68px; top: 230px; width: 173px;
    text-align: center; font-size: 9px; letter-spacing: 2.5px; text-transform: uppercase;
  }

  .panel-top { position: absolute; left: 280px; top: 66px; width: 523px; height: 206px; background: var(--panel); }
  .panel-main { position: absolute; left: 36px; top: 268px; width: 767px; height: 884px; background: var(--panel); }

  .address {
    position: absolute; left: 300px; top: 90px; width: 240px;
    text-align: center; font-weight: 700; font-size: 47px; line-height: 58px;
  }

  .ribbon { position: absolute; left: 560px; top: 50px; width: 260px; height: 272px; }

  .price {
    position: absolute; left: 36px; top: 308px; width: 767px;
    text-align: center; font-weight: 700; font-size: 67px; line-height: 80px; white-space: nowrap;
  }

  .description { position: absolute; left: 104px; top: 424px; width: 680px; }
  .description-title { font-weight: 700; font-size: 28px; line-height: 32px; }
  .description-body { font-weight: 700; font-size: 23.5px; line-height: 31px; white-space: nowrap; }

  .features { position: absolute; left: 0; top: 574px; width: 848px; height: 100px; }
  .feature { position: absolute; display: flex; align-items: center; gap: 8px; }
  .feature-icon { width: 62px; height: 62px; }
  .feature-count { font-weight: 700; font-size: 80px; line-height: 90px; }
  .feature.bed { left: 114px; top: 10px; }
  .feature.bath { left: 344px; top: 10px; }
  .feature.car { left: 574px; top: -4px; }

  .photo {
    position: absolute; border: 3px solid var(--white); border-radius: 3px;
  }
  .photo.kitchen { left: 74px; top: 709px; width: 164px; height: 162px;
    background: linear-gradient(160deg, #e9ece8 0%, #c9cbc4 45%, #8a5a3a 75%, #b9bdb5 100%); }
  .photo.living { left: 259px; top: 709px; width: 322px; height: 341px;
    background: linear-gradient(180deg, #3a3d3c 0%, #9fa7a6 25%, #5b3a2f 55%, #23201e 75%, #d8d8d2 100%); }
  .photo.bedroom { left: 598px; top: 709px; width: 165px; height: 161px;
    background: linear-gradient(170deg, #f1f1ec 0%, #d4d3cb 50%, #7a5f48 75%, #c9c8c0 100%); }
  .photo.dining { left: 74px; top: 886px; width: 164px; height: 164px;
    background: linear-gradient(150deg, #dfe2de 0%, #b4b8b0 40%, #6d4a33 70%, #4d6a33 100%); }
  .photo.tap { left: 600px; top: 886px; width: 165px; height: 165px;
    background: radial-gradient(circle at 60% 40%, #e6e8e6 0%, #9aa3a8 40%, #4f5a62 75%, #2c3338 100%); }
</style>
</head>
<body>
<main class="card">
  <div class="panel-top"></div>
  <div class="panel-main"></div>

  <header class="brand">
    <span class="brand-name">K7<br>Residences</span>
  </header>
  <p class="brand-architect">By Marlow Reid</p>

  <h1 class="address">Address Entered Here</h1>

  <svg class="ribbon" viewBox="0 0 260 272" aria-label="For sale">
    <polygon points="243,255 255,255 255,272" fill="var(--olive-dark)"/>
    <polygon points="3,2 80,2 255,178 255,256" fill="var(--olive)"/>
    <text x="0" y="0" transform="translate(124,110) rotate(45)" text-anchor="middle"
          font-family="Arimo, Arial, sans-serif" font-weight="700" font-size="42" fill="#fff">FOR SALE</text>
  </svg>

  <h2 class="price">$ Price entered here</h2>

  <section class="description">
    <h3 class="description-title">Description:</h3>
    <p class="description-body">text, text, text, text, text, text, texttext, text, text, text,<br>text, text, texttext, text, text, text, text, text, text<br>text, text, text, text, text, text, text</p>
  </section>

  <section class="features">
    <div class="feature bed">
      <svg class="feature-icon" viewBox="0 0 62 62" aria-label="Bedrooms">
        <circle cx="31" cy="31" r="28" fill="var(--olive)" stroke="#fff" stroke-width="3"/>
        <rect x="14" y="22" width="3" height="20" fill="#fff"/>
        <rect x="17" y="31" width="31" height="6" fill="#fff"/>
        <rect x="45" y="34" width="3" height="8" fill="#fff"/>
        <rect x="19" y="26" width="8" height="5" rx="2" fill="#fff"/>
      </svg>
      <span class="feature-count">3</span>
    </div>
    <div class="feature bath">
      <svg class="feature-icon" viewBox="0 0 62 62" aria-label="Bathrooms">
        <circle cx="31" cy="31" r="28" fill="var(--olive)" stroke="#fff" stroke-width="3"/>
        <path d="M14 32 H48 V36 Q48 44 40 44 H22 Q14 44 14 36 Z" fill="#fff"/>
        <path d="M18 32 V20 Q18 16 22 16 Q26 16 26 20" fill="none" stroke="#fff" stroke-width="3"/>
        <rect x="20" y="44" width="3" height="4" fill="#fff"/>
        <rect x="39" y="44" width="3" height="4" fill="#fff"/>
      </svg>
      <span class="feature-count">2</span>
    </div>
    <div class="feature car">
      <svg class="feature-icon" viewBox="0 0 62 62" aria-label="Car spaces">
        <circle cx="31" cy="31" r="28" fill="var(--olive)" stroke="#fff" stroke-width="3"/>
        <path d="M16 30 L20 20 H42 L46 30 V40 H16 Z" fill="#fff"/>
        <path d="M22 22 H40 L43 29 H19 Z" fill="var(--olive)"/>
        <circle cx="22" cy="34" r="2.5" fill="var(--olive)"/>
        <circle cx="40" cy="34" r="2.5" fill="var(--olive)"/>
        <rect x="17" y="40" width="6" height="5" fill="#fff"/>
        <rect x="39" y="40" width="6" height="5" fill="#fff"/>
      </svg>
      <span class="feature-count">1</span>
    </div>
  </section>

  <div class="photo kitchen" role="img" aria-label="Photo of the open-plan kitchen"></div>
  <div class="photo living" role="img" aria-label="Photo of the living room with sofa and tall window"></div>
  <div class="photo bedroom" role="img" aria-label="Photo of the bedroom"></div>
  <div class="photo dining" role="img" aria-label="Photo of the dining area and balcony"></div>
  <div class="photo tap" role="img" aria-label="Close-up photo of the kitchen tap"></div>
</main>
</body>
</html>
```